Maple Cove Laser Dermal Studio needs an 8 page WP redesign

We need a colorful re-design for an 8 page Wordpress website. The current preliminary website is live. The home page URL is http://maplecovelaserdermalstudio.com The new logo is live on the website also. I would like a (re)design using the colors that are represented by the new logo file, and any additional complimentary colors. The information regarding the business can be found on the website already, so please review it for insight. The name of the business is "Maple Cove Laser Dermal Studio".

Target Market(s)

The targeted website viewer is an adult female between the ages of 30 and 75 who is interested in facial renewal, wart removal and scar removal. This website should inspire in the target viewer the benefits of laser facial renewal, wart removal and new scar removal. Potential website viewers are wanting and searching for improved skin health and appearance. The website must represent the essence of a professional spa business.

Industry/Entity Type

Business

Font styles to use
Sans Serif

Requirements
Must have
• - The phone number placed in a visible and high value widget area that allows mobile phone browser dialing.

```html
<!DOCTYPE html>
<html lang="en">
<head>
<meta charset="utf-8">
<title>Maple Cove Laser Dermal Studio</title>
<link href="https://fonts.googleapis.com/css2?family=Open+Sans:wght@400;600;700;800&display=swap" rel="stylesheet">
<style>
:root{
  --purple:#9a2a8e;
  --magenta:#b53aa6;
  --purple-deep:#6e1c66;
  --ink:#333;
  --muted:#777;
  --paper:#fff;
  --soft:#f4f1f4;
  --night:#231a22;
  --footer:#2f2430;
  --footer-text:#a99aa7;
  --bar:#1a1419;
}
*{box-sizing:border-box;margin:0;padding:0}
html,body{width:835px;height:1200px;overflow:hidden}
body{font-family:"Open Sans",Arial,sans-serif;color:var(--ink);background:var(--paper);position:relative}
.header{height:110px;position:relative;background:var(--paper)}
.brand{position:absolute;left:22px;top:24px;display:flex;align-items:center;gap:10px}
.brand-dot{width:16px;height:16px;border-radius:50%;background:var(--purple)}
.brand-name{font-size:17px;font-weight:700;color:var(--purple);line-height:1.15;width:170px}
.nav{position:absolute;left:436px;top:66px;display:flex;gap:2px;white-space:nowrap}
.nav a{font-size:10px;color:var(--ink);text-decoration:none;padding:5px 10px;line-height:1.2}
.nav a.active{background:var(--purple-deep);color:#fff;border-radius:3px}
.call{position:absolute;right:28px;top:10px;text-align:right;line-height:1.3}
.social{display:flex;gap:5px;justify-content:flex-end;margin-bottom:4px}
.social span{width:14px;height:14px;border-radius:50%;background:var(--purple)}
.call-label{font-size:12px;font-weight:700;color:var(--ink);white-space:nowrap}
.call-phone{display:block;font-size:12px;color:var(--purple);font-weight:600;text-decoration:none}
.hero{position:absolute;top:110px;left:0;width:835px;height:290px;background:linear-gradient(90deg,#f3e8ee 0%,#fbf7f9 55%,#fff 100%)}
.hero-photo{position:absolute;left:0;top:0;width:400px;height:290px;background:radial-gradient(ellipse at 55% 45%,#f1d3c6 0%,#e9c0b2 35%,#f3e4e8 70%,#f7eef2 100%)}
.hero-copy{position:absolute;left:428px;top:52px;width:395px}
.hero-copy h1{font-size:26px;font-weight:400;color:var(--ink);line-height:1.15}
.hero-copy h2{font-size:22px;font-weight:600;color:var(--purple);line-height:1.3;white-space:nowrap}
.hero-copy .lead{font-size:13px;font-weight:700;color:var(--ink);margin:6px 0 10px;line-height:1.3}
.hero-copy p{font-size:9px;color:var(--muted);line-height:1.5}
.book{display:flex;align-items:center;gap:8px;margin-top:14px;font-size:13px;color:var(--purple);font-weight:600;text-decoration:none}
.services{position:absolute;top:400px;left:0;width:835px;height:60px;background:linear-gradient(180deg,var(--magenta),var(--purple));display:flex;justify-content:space-around;align-items:center;padding:0 30px}
.service{display:flex;align-items:center;gap:8px;color:#fff}
.service-icon{width:34px;height:34px;border-radius:50%;border:2px solid rgba(255,255,255,.7);background:rgba(255,255,255,.15)}
.service b{display:block;font-size:14px;font-weight:600}
.service small{font-size:8px;opacity:.85}
.showcase{position:absolute;top:460px;left:0;width:835px;height:210px;background:radial-gradient(ellipse at 50% 40%,#3d2a3a 0%,var(--night) 75%)}
.card{position:absolute;top:18px;width:200px;height:176px;background:var(--paper);border:3px solid #fff;display:flex}
.card-text{width:50%;padding:22px 8px 0 10px}
.card-text h3{font-size:16px;font-weight:700;color:var(--ink);line-height:1.2}
.card-text .more{display:block;margin-top:18px;width:22px;height:22px;border-radius:50%;background:var(--purple)}
.card-photo{width:50%;height:100%}
.welcome{position:absolute;top:670px;left:0;width:835px;height:145px;background:var(--soft)}
.welcome-main{position:absolute;left:70px;top:14px;width:430px}
.welcome-main h2{font-size:15px;font-weight:400;color:var(--ink);white-space:nowrap;line-height:1.3}
.welcome-main h2 em{font-style:normal;color:var(--purple);font-weight:600}
.welcome-main p{font-size:8px;color:var(--muted);line-height:1.45;margin-top:5px}
.welcome-main p.accent{color:var(--purple)}
.btn{display:inline-block;margin-top:8px;background:var(--purple);color:#fff;font-size:10px;font-weight:600;padding:5px 11px;border-radius:2px;text-decoration:none;line-height:1.3}
.welcome-side{position:absolute;left:515px;top:20px;width:255px}
.welcome-side p{font-size:8px;color:var(--muted);line-height:1.5}
.video{margin-top:8px;margin-left:45px;width:210px;height:56px;background:linear-gradient(120deg,#6b4a3c,#b08a6f 55%,#d9c1a8)}
.partners{position:absolute;top:815px;left:0;width:835px;height:115px;background:var(--paper);display:flex;justify-content:center;align-items:center;gap:34px}
.partner{height:18px;background:#d6d3d6;border-radius:3px}
.newsletter{position:absolute;top:930px;left:0;width:835px;height:55px;background:var(--bar);display:flex;align-items:center;padding:0 40px}
.newsletter h4{font-size:14px;font-weight:700;color:#fff;letter-spacing:.3px}
.newsletter small{display:block;font-size:8px;color:#aaa;font-weight:400}
.field{margin-left:auto;width:160px;height:22px;background:#fff;border-radius:2px;font-size:8px;color:#999;padding:5px 8px}
.field+.field{margin-left:10px}
.subscribe{margin-left:10px;background:var(--purple);color:#fff;font-size:10px;font-weight:700;padding:5px 16px;border-radius:2px}
.footer{position:absolute;top:985px;left:0;width:835px;height:185px;background:var(--footer);display:flex;padding:18px 40px 0;gap:26px}
.col{width:171px}
.col h5{font-size:10px;font-weight:700;color:#fff;letter-spacing:.5px;margin-bottom:8px}
.col p{font-size:8px;color:var(--footer-text);line-height:1.6}
.col .row{display:flex;gap:6px;align-items:center;font-size:8px;color:var(--footer-text);line-height:1.9;white-space:nowrap}
.ico{width:8px;height:8px;border-radius:50%;background:var(--magenta);flex:none}
.foot-social{display:flex;gap:5px;margin-top:10px}
.foot-social span{width:14px;height:14px;border-radius:50%;background:#5a4858}
.bottom{position:absolute;top:1170px;left:0;width:835px;height:30px;background:var(--bar);display:flex;align-items:center;padding:0 40px;font-size:8px;color:#8c808a}
.bottom nav{margin-left:auto;display:flex;gap:24px}
</style>
</head>
<body>
<header class="header">
  <div class="brand"><span class="brand-dot"></span><span class="brand-name">Maple Cove Laser Dermal Studio</span></div>
  <div class="call">
    <div class="social"><span></span><span></span><span></span></div>
    <div class="call-label">YOU CALL, WE'RE THERE</div>
    <a class="call-phone" href="tel:08005550147">(0800) 555 0147</a>
  </div>
  <nav class="nav">
    <a class="active" href="#">Home</a><a href="#">About Us</a><a href="#">Laser Renewal</a><a href="#">Services</a><a href="#">Blog</a><a href="#">Contact</a>
  </nav>
</header>

<section class="hero">
  <div class="hero-photo" role="img" aria-label="Portrait photo of a woman with smooth skin touching her cheek"></div>
  <div class="hero-copy">
    <h1>Welcome To The</h1>
    <h2>Maple Cove Laser Dermal Studio</h2>
    <div class="lead">Lorem ipsum dolor sit amet consectetur adipiscing elit.</div>
    <p>Lorem ipsum est simplement du faux texte employé dans la mise en page avant impression. Le lorem ipsum est le faux texte standard de l'imprimerie depuis les années mille cinq cents, quand un peintre anonyme assembla des morceaux.</p>
    <a class="book" href="#"><svg width="20" height="20" viewBox="0 0 20 20"><circle cx="10" cy="10" r="10" fill="#9a2a8e"/><path d="M8 6l4 4-4 4" stroke="#fff" stroke-width="2" fill="none"/></svg>Book Online</a>
  </div>
</section>

<section class="services">
  <div class="service"><span class="service-icon"></span><div><b>Skin Renewal</b><small>Lorem ipsum dolor</small></div></div>
  <div class="service"><span class="service-icon"></span><div><b>Wart Renewal</b><small>Lorem ipsum dolor</small></div></div>
  <div class="service"><span class="service-icon"></span><div><b>Scar Renewal</b><small>Lorem ipsum dolor</small></div></div>
  <div class="service"><span class="service-icon"></span><div><b>Anti Aging</b><small>Lorem ipsum dolor</small></div></div>
</section>

<section class="showcase">
  <article class="card" style="left:105px">
    <div class="card-text"><h3>Skin &amp; Lazer Renewal</h3><span class="more"></span></div>
    <div class="card-photo" role="img" aria-label="Photo of a woman receiving a facial treatment" style="background:linear-gradient(160deg,#e8d6cf,#c9a595)"></div>
  </article>
  <article class="card" style="left:318px">
    <div class="card-text"><h3>Skin &amp; Lazer Renewal</h3><span class="more"></span></div>
    <div class="card-photo" role="img" aria-label="Photo of a woman with dark hair" style="background:linear-gradient(160deg,#6a4b43,#d3b2a2)"></div>
  </article>
  <article class="card" style="left:532px">
    <div class="card-text"><h3>Skin &amp; Lazer Renewal</h3><span class="more"></span></div>
    <div class="card-photo" role="img" aria-label="Photo of a laser skin treatment" style="background:linear-gradient(160deg,#d9c3bb,#a98477)"></div>
  </article>
</section>

<section class="welcome">
  <div class="welcome-main">
    <h2>Welcome to the <em>Maple Cove Laser Dermal Studio</em></h2>
    <p>Lorem ipsum est simplement du faux texte employé dans la composition et la mise en page avant impression. Le lorem ipsum est le faux texte standard de l'imprimerie depuis les années quinze cents, quand un imprimeur anonyme assembla des morceaux de texte.</p>
    <p class="accent">Il n'a pas fait que survivre cinq siècles, mais s'est aussi adapté à la bureautique.</p>
    <a class="btn" href="#">Book An Appointment</a>
  </div>
  <div class="welcome-side">
    <p>Lorem ipsum est simplement du faux texte employé dans la composition et la mise en page avant impression, sans que son contenu soit modifié.</p>
    <div class="video" role="img" aria-label="Video thumbnail of a relaxing spa treatment room"></div>
  </div>
</section>

<section class="partners" aria-label="Partner brands">
  <span class="partner" style="width:70px"></span>
  <span class="partner" style="width:56px"></span>
  <span class="partner" style="width:80px"></span>
  <span class="partner" style="width:60px"></span>
  <span class="partner" style="width:86px"></span>
</section>

<section class="newsletter">
  <h4>SIGN UP TO A NEWSLETTER<small>Lorem ipsum dolor sit amet adipiscing elit</small></h4>
  <div class="field">Name</div>
  <div class="field">Email</div>
  <div class="subscribe">SUBSCRIBE</div>
</section>

<footer class="footer">
  <div class="col">
    <h5>WHO WE ARE</h5>
    <p>Lorem ipsum dolor sit amet, consectetur adipiscing elit. Nullam quis nibh nunc. Donec varius velit quis ante semper, vitae tincidunt nulla euismod. Cras sit amet metus.</p>
  </div>
  <div class="col">
    <h5>WHAT WE DO</h5>
    <p>Lorem ipsum dolor sit amet, consectetur adipiscing elit. Integer fermentum massa vel lectus faucibus, non blandit nibh rhoncus. Sed vitae mauris.</p>
  </div>
  <div class="col">
    <h5>CONTACT US</h5>
    <div class="row"><span class="ico"></span>48 Harbor Lane, Maple Cove</div>
    <div class="row"><span class="ico"></span>(0800) 555 0147</div>
    <div class="row"><span class="ico"></span>hello@maplecovedermal.com</div>
    <div class="row"><span class="ico"></span>maplecovelaserdermalstudio.com</div>
  </div>
  <div class="col">
    <h5>GET IN TOUCH</h5>
    <p>If you have any questions you can reach us on the number below or follow us on social media.</p>
    <div class="foot-social"><span></span><span></span><span></span><span></span></div>
  </div>
</footer>

<div class="bottom">
  <span>Copyright © 2013 Maple Cove Laser Dermal Studio. All Rights Reserved</span>
  <nav><span>Terms &amp; Conditions</span><span>Privacy Policy</span></nav>
</div>
</body>
</html>
```